Corvanlit.media

I need a full page PSD made (desktop and mobile view) with a layout similar to what I have in my text file, but a smooth flowing, good looking design. Only take my text file as an idea of order things show flow. I have taken my exact steps from the text file, put them together, and it did not look good, which is why I am seeking a professional design.

```html
<!DOCTYPE html>
<html lang="en">
<head>
<meta charset="utf-8">
<title>Corvanlit.media — Reviews and Text Marketing</title>
<link rel="stylesheet" href="https://fonts.googleapis.com/css2?family=Poppins:wght@400;500;600;700&display=swap">
<style>
  :root{
    --blue:#1767dc;
    --blue-dark:#1156c4;
    --ink:#222a36;
    --text:#3d4350;
    --muted:#5b6270;
    --panel:#f3f3f3;
    --page:#fafafa;
    --footer:#2b2b2b;
    --white:#ffffff;
  }
  *{box-sizing:border-box;margin:0;padding:0}
  html,body{width:1200px;height:3624px;overflow:hidden}
  body{position:relative;background:var(--page);font-family:"Poppins",sans-serif;color:var(--text)}
  .abs{position:absolute}

  /* header */
  .site-header{left:0;top:0;width:1200px;height:107px;background:var(--white);border-bottom:2px solid #e6e8ec}
  .brand{left:111px;top:26px;font-size:30px;font-weight:700;color:var(--ink);letter-spacing:-.5px;display:flex;align-items:center;gap:10px}
  .brand-dot{width:12px;height:12px;background:var(--blue);border-radius:50%}
  .nav a{position:absolute;top:42px;font-size:15px;font-weight:500;color:var(--ink);text-decoration:none}
  .nav a.active{color:var(--blue)}
  .nav a.active::after{content:"";position:absolute;left:-2px;right:-2px;bottom:-8px;height:2px;background:var(--blue);border-radius:2px}

  /* hero */
  .hero{left:0;top:109px;width:1200px;height:659px;background:linear-gradient(110deg,#eaf2fb 0%,#f6f9fd 45%,#ffffff 70%,#eef4fb 100%)}
  .hero-title{left:112px;top:262px;width:520px;font-size:46px;line-height:63px;font-weight:700;color:var(--blue)}
  .hero-tag{left:112px;top:463px;font-size:22px;color:var(--ink)}
  .btn{display:flex;align-items:center;justify-content:center;gap:30px;background:var(--blue);color:var(--white);font-weight:500;text-decoration:none;border-radius:3px}
  .hero-btn{left:112px;top:527px;width:172px;height:50px;font-size:16px}
  .hero-photo-frame{left:634px;top:165px;width:453px;height:545px;background:var(--white);padding:7px;box-shadow:0 2px 8px rgba(0,0,0,.15)}
  .photo{width:100%;height:100%}
  .hero-photo{background:linear-gradient(160deg,#6f98b8 0%,#b49b86 40%,#5a6875 70%,#3c4a55 100%)}

  /* how it works */
  .section-title{font-size:36px;font-weight:700;color:var(--blue)}
  .section-sub{font-size:19px;color:var(--text)}
  .center{left:0;width:1200px;text-align:center}
  .step-title{font-size:30px;font-weight:600;color:var(--blue)}
  .step-text{font-size:21px;line-height:37px;color:var(--text)}

  .step-one{left:111px;top:927px;width:976px;height:426px;background:var(--blue)}
  .step-one .step-title,.step-one .step-text{color:var(--white)}
  .step-one-photo{left:566px;top:969px;width:488px;height:343px;border:1px solid #d9dde3;background:linear-gradient(90deg,#3d3a38 0%,#5b4b40 30%,#e2e2e4 48%,#eeeef0 100%)}

  .panel{background:var(--panel)}
  .phone{border-radius:34px;background:linear-gradient(180deg,#f1f1f3,#dcdde0);border:2px solid #c9cbd0}

  /* text marketing */
  .sms-band{left:0;top:2353px;width:1200px;height:506px;background:#f5f6f8}
  .sms-photo{left:0;top:2353px;width:605px;height:506px;background:linear-gradient(120deg,#c7d3df 0%,#e7ebef 35%,#2b2d31 60%,#d7a88f 100%)}
  .ticks{list-style:none;left:634px;top:2574px;width:470px}
  .ticks li{position:relative;padding-left:32px;font-size:15px;line-height:24px;color:var(--text);margin-bottom:28px}
  .ticks svg{position:absolute;left:2px;top:6px}

  /* pricing */
  .pricing{left:0;top:2859px;width:1200px;height:678px;background:var(--blue)}
  .price-card{left:423px;top:3016px;width:355px;height:521px;background:var(--white)}
  .price{left:423px;top:3060px;width:355px;text-align:center;color:var(--blue);font-size:66px;font-weight:600;line-height:80px}
  .price sup{font-size:20px;color:var(--ink);vertical-align:top;position:relative;top:16px}
  .price small{font-size:26px;font-weight:400;color:var(--ink)}
  .price-rule{left:423px;top:3151px;width:355px;height:1px;background:#e4e6ea}
  .features{list-style:none;left:494px;top:3176px}
  .features li{position:relative;padding-left:30px;font-size:15px;color:var(--text);height:57.5px}
  .features svg{position:absolute;left:0;top:6px}
  .select-btn{left:513px;top:3461px;width:174px;height:48px;font-size:17px;gap:24px;border-radius:2px}

  .site-footer{left:0;top:3537px;width:1200px;height:87px;background:var(--footer);color:var(--white);font-size:17px;text-align:center;line-height:87px}
</style>
</head>
<body>

<header class="site-header abs">
  <div class="brand abs"><span>Corvanlit.media</span><span class="brand-dot"></span></div>
  <nav class="nav">
    <a class="active" href="#" style="left:599px">Home</a>
    <a href="#" style="left:696px">Pricing</a>
    <a href="#" style="left:802px">Login</a>
    <a href="#" style="left:895px">Signup</a>
    <a href="#" style="left:1000px">Contact Us</a>
  </nav>
</header>

<section class="hero abs"></section>
<h1 class="hero-title abs">Get 5 Star Reviews and Text Message Marketing</h1>
<p class="hero-tag abs">All in one tool!</p>
<a class="btn hero-btn abs" href="#">Get Started
  <svg width="8" height="12" viewBox="0 0 8 12"><path d="M2 2l4 4-4 4" fill="none" stroke="#fff" stroke-width="1.6"/></svg>
</a>
<div class="hero-photo-frame abs">
  <div class="photo hero-photo" role="img" aria-label="Hand tapping a smartphone screen against blurred city lights"></div>
</div>

<h2 class="section-title abs center" style="top:817px">How It Works</h2>
<p class="section-sub abs center" style="top:870px">5 Star Review System</p>

<section class="step-one abs"></section>
<h3 class="step-title abs" style="left:187px;top:1052px">Step : 01</h3>
<p class="step-text abs" style="left:187px;top:1108px;width:350px;color:#fff">You display an offer near your cash register.</p>
<div class="step-one-photo abs" role="img" aria-label="Counter sign by a cash register offering 50% off for texting a keyword"></div>

<div class="panel abs" style="left:439px;top:1488px;width:560px;height:287px"></div>
<div class="phone abs" style="left:204px;top:1411px;width:232px;height:432px" role="img" aria-label="Phone showing a text message review conversation"></div>
<h3 class="step-title abs" style="left:508px;top:1577px">Step : 02</h3>
<p class="step-text abs" style="left:508px;top:1632px">Customer starts the review sequence</p>

<div class="panel abs" style="left:196px;top:1920px;width:571px;height:289px"></div>
<div class="phone abs" style="left:768px;top:1854px;width:234px;height:433px" role="img" aria-label="Phone showing a new five star review notification"></div>
<h3 class="step-title abs" style="left:249px;top:2010px">Step : 03</h3>
<p class="step-text abs" style="left:249px;top:2066px">Your business earns 5 star reviews!</p>

<section class="sms-band abs"></section>
<div class="sms-photo abs" role="img" aria-label="Hand holding a phone showing a promotional text message from a shop"></div>
<h2 class="section-title abs" style="left:634px;top:2458px">How It Works</h2>
<p class="section-sub abs" style="left:634px;top:2510px">Text Marketing System</p>
<ul class="ticks abs">
  <li><svg width="13" height="10" viewBox="0 0 13 10"><path d="M1 5l4 4 7-8" fill="none" stroke="#1767dc" stroke-width="2"/></svg>Phone numbers are collected from Cash Register Offer.</li>
  <li><svg width="13" height="10" viewBox="0 0 13 10"><path d="M1 5l4 4 7-8" fill="none" stroke="#1767dc" stroke-width="2"/></svg>Simply log into the dashboard and send all your customers a text message of any specials or promotions.</li>
  <li><svg width="13" height="10" viewBox="0 0 13 10"><path d="M1 5l4 4 7-8" fill="none" stroke="#1767dc" stroke-width="2"/></svg>Watch your customer come through the door!</li>
</ul>

<section class="pricing abs"></section>
<h2 class="section-title abs center" style="top:2896px;color:#fff">Pricing</h2>
<p class="section-sub abs center" style="top:2948px;color:#fff">Simple Price. All the Benefits.</p>
<div class="price-card abs"></div>
<p class="price abs"><sup>$</sup>149<small>/mo</small></p>
<div class="price-rule abs"></div>
<ul class="features abs">
  <li><svg width="13" height="10" viewBox="0 0 13 10"><path d="M1 5l4 4 7-8" fill="none" stroke="#1767dc" stroke-width="2"/></svg>Customer Review System</li>
  <li><svg width="13" height="10" viewBox="0 0 13 10"><path d="M1 5l4 4 7-8" fill="none" stroke="#1767dc" stroke-width="2"/></svg>Text Message Marketing</li>
  <li><svg width="13" height="10" viewBox="0 0 13 10"><path d="M1 5l4 4 7-8" fill="none" stroke="#1767dc" stroke-width="2"/></svg>Customer Feedback</li>
  <li><svg width="13" height="10" viewBox="0 0 13 10"><path d="M1 5l4 4 7-8" fill="none" stroke="#1767dc" stroke-width="2"/></svg>Email Notifications</li>
  <li><svg width="13" height="10" viewBox="0 0 13 10"><path d="M1 5l4 4 7-8" fill="none" stroke="#1767dc" stroke-width="2"/></svg>Online Dashboard</li>
</ul>
<a class="btn select-btn abs" href="#">SELECT
  <svg width="18" height="18" viewBox="0 0 18 18"><circle cx="9" cy="9" r="8" fill="#fff"/><path d="M7.5 5.5L11 9l-3.5 3.5" fill="none" stroke="#1767dc" stroke-width="2"/></svg>
</a>

<footer class="site-footer abs">© Copyright-2020 Corvanlit Media. All rights reserved.</footer>

</body>
</html>
```